Covid 19 Exit Strategy one page brochure

I would like to design, and will need URGENT help, a brochure detailing a Covid 19 Exit Strategy plan. This brochure will need to be understood easily and the graphics inside should make it easy for people to understand without reading the entire text. This project is quite urgent and needs to be completed THIS WEEK - by Saturday may 16th at the latest. I am attaching two examples. I will provide the text.

```html
<!DOCTYPE html>
<html lang="en">
<head>
<meta charset="utf-8">
<title>COVID-19 Phased Exit Strategy</title>
<link href="https://fonts.googleapis.com/css2?family=Oswald:wght@500;700&family=Montserrat:wght@400;500;600;700;800&display=swap" rel="stylesheet">
<style>
:root{
  --bg:#d6d6d6;
  --page:#ffffff;
  --blue:#4a8fe0;
  --blue-dark:#3b7fd6;
  --blue-pale:#dceafb;
  --purple:#8c7cf0;
  --ink:#3a3a3a;
  --text:#555a60;
  --orange:#f26a2e;
  --orange-head:#ef6a2b;
  --peach:#fbb593;
  --peach-light:#fbd9a6;
}
*{box-sizing:border-box;margin:0;padding:0}
html,body{width:751px;height:1200px;overflow:hidden;background:var(--bg)}
body{font-family:'Montserrat',Arial,sans-serif;color:var(--text);position:relative}
.sheet{position:absolute;left:170px;width:410px;height:582px;overflow:hidden;box-shadow:0 2px 6px rgba(0,0,0,.15)}
.sheet--front{top:12px}
.sheet--back{top:606px}
.page{position:absolute;left:0;top:0;width:591px;height:838px;background:var(--page);transform:scale(.6937);transform-origin:0 0;overflow:hidden}
.abs{position:absolute}
.art{position:absolute;border-radius:50%}

/* front */
.title{left:40px;top:52px;font-family:'Oswald',Impact,sans-serif;font-weight:700;font-size:66px;line-height:1;color:var(--ink);letter-spacing:-1px}
.title span{color:var(--blue)}
.subtitle{left:42px;top:128px;font-weight:700;font-size:25px;color:var(--blue)}
.byline{left:48px;top:162px;font-size:14px;color:var(--ink)}
.byline b{color:var(--blue);font-weight:700}
.hero{left:285px;top:0;width:306px;height:250px;border-radius:0 0 0 120px;background:linear-gradient(135deg,#8fd3f7 0%,#4a8fe0 55%,#8c7cf0 100%)}
.req-bar{left:40px;top:212px;width:288px;height:38px;background:var(--blue);color:#fff;font-size:19px;font-weight:600;padding:7px 0 0 8px;letter-spacing:.3px}
.req-bar b{font-weight:800}
.req-head{font-family:'Oswald',Impact,sans-serif;font-weight:500;color:var(--orange-head);font-size:13px;line-height:1.25;text-transform:uppercase}
.req-text{font-size:7.6px;line-height:1.3;color:var(--text)}
.panel{left:320px;top:278px;width:235px;height:498px;background:var(--peach);border-radius:20px}
.panel-item{position:absolute;left:22px;width:206px;display:flex;align-items:flex-start;gap:12px}
.icon-ring{flex:none;width:54px;height:54px;border-radius:50%;background:#fff;border:3px solid #fde5d8;display:flex;align-items:center;justify-content:center}
.icon-ring i{display:block;width:34px;height:34px;border-radius:50%;background:linear-gradient(135deg,#f7b1b1,#e8414c)}
.panel-item p{color:#fff;font-size:7.4px;line-height:1.35;font-weight:600;padding-top:6px}
.blob-bl{left:-40px;top:735px;width:260px;height:130px;border-radius:50%;background:linear-gradient(90deg,#8c7cf0,#a7b8f5)}
.base-line{left:0;top:828px;width:591px;height:10px;background:linear-gradient(90deg,var(--blue),var(--purple))}
.dots{border-top:1.5px dotted #777}

/* back */
.header{left:0;top:0;width:591px;height:78px;background:var(--blue);color:#fff;text-align:center;font-weight:800;font-size:21px;line-height:26px;padding-top:13px}
.stage-tag{background:var(--blue-pale);color:var(--blue);font-weight:700;font-size:20px;padding:4px 16px;height:34px}
.lead{font-size:8.4px;font-weight:600;color:#444;line-height:1.3}
.seq-head{color:var(--orange);font-weight:700;font-size:14px;line-height:1.2}
.seq{position:absolute;list-style:none}
.seq li{display:flex;gap:7px;font-size:7.4px;line-height:1.3;color:var(--text)}
.seq li em{font-style:normal;font-family:'Oswald',sans-serif;font-size:17px;line-height:1;color:#9aa0a8;flex:none;width:17px}
.stage-col{position:absolute;display:flex;flex-direction:column;gap:8px}
.stage-col .seq-head{font-size:12.5px}
.stage-col .seq{position:static}
.stage-col .seq li{padding-bottom:6px}
.divider{left:293px;top:440px;width:1px;height:370px;background:#cfd8e6}
.blob-br{left:520px;top:800px;width:160px;height:90px;border-radius:50%;background:linear-gradient(135deg,#a7b8f5,#8c7cf0)}
</style>
</head>
<body>

<section class="sheet sheet--front">
  <div class="page">
    <div class="abs hero" role="img" aria-label="Illustration of a globe with virus particles, leaves and a group of people wearing masks"></div>
    <h1 class="abs title">COVID-<span>19</span></h1>
    <div class="abs subtitle">Phased Exit Strategy</div>
    <div class="abs byline">Developed by <b>Lena Varga</b></div>
    <div class="abs req-bar"><b>GENERAL</b> REQUIREMENTS</div>

    <div class="art" style="left:42px;top:275px;width:112px;height:112px;background:var(--peach-light)" role="img" aria-label="Illustration of patients in hospital beds"></div>
    <div class="abs dots" style="left:130px;top:278px;width:100px"></div>
    <div class="abs" style="left:178px;top:298px;width:130px">
      <div class="req-head">Documented cases</div>
      <p class="req-text">Single digit downward trend of documented cases within the past 14days.</p>
    </div>

    <div class="abs" style="left:40px;top:410px;width:125px;height:85px;border-radius:40px;background:linear-gradient(90deg,#cfe9fb,#8fc6f2)" role="img" aria-label="Illustration of health workers moving a patient on a stretcher"></div>
    <div class="abs dots" style="left:100px;top:402px;width:62px"></div>
    <div class="abs" style="left:172px;top:403px;width:130px">
      <div class="req-head">Hospitals and<br>the health care</div>
      <p class="req-text">Hospitals and the health care system are capable of treating patients without operating on a crisis mode.</p>
    </div>

    <div class="abs dots" style="left:140px;top:532px;width:55px"></div>
    <div class="abs" style="left:60px;top:542px;width:130px">
      <div class="req-head">Ability to surge ICU</div>
      <p class="req-text">Ability to surge ICU capacity on a short notice - 24h.</p>
    </div>
    <div class="art" style="left:195px;top:515px;width:110px;height:110px;background:var(--peach-light)" role="img" aria-label="Illustration of a doctor beside an IV drip stand"></div>

    <div class="abs" style="left:48px;top:625px;width:110px;height:140px;border-radius:30px;background:linear-gradient(180deg,#e7d2c0,#3f7fd1)" role="img" aria-label="Illustration of a person in a mask and scarf coughing"></div>
    <div class="abs" style="left:170px;top:648px;width:128px">
      <div class="req-head">Symptomatic</div>
      <p class="req-text">Ability to screen and test symptomatic individuals within 24 hours of identification. Increased and sufficient testing capacity, to test at least 50% of all population if necessary within a timeframe of 3 months.</p>
    </div>
    <div class="abs dots" style="left:150px;top:770px;width:95px"></div>

    <div class="abs panel">
      <div class="panel-item" style="top:30px"><div class="icon-ring" role="img" aria-label="Virus particles icon"><i></i></div><p>Plan in place to trigger targeted or full-scale containment in case of sudden outbreaks</p></div>
      <div class="panel-item" style="top:105px"><div class="icon-ring"><svg width="34" height="34" viewBox="0 0 34 34" aria-hidden="true"><circle cx="17" cy="17" r="16" fill="#fff" stroke="#f3c9c9" stroke-width="2"/><path d="M13 6h8v7h7v8h-7v7h-8v-7H6v-8h7z" fill="#e8414c"/></svg></div><p>Mandatory use of masks (at least surgical grade) for everyone in all public areas and at work. Mandatory use of N95, or equivalent, masks for all healthcare front workers and for all government agencies and authorities that are involved in overseeing the containment activities.</p></div>
      <div class="panel-item" style="top:225px"><div class="icon-ring" role="img" aria-label="Thermometer temperature check icon"><i style="background:linear-gradient(135deg,#d7e6f8,#e8414c)"></i></div><p>Mandatory daily checks of body temperature for everyone at the workplace or entering public areas.</p></div>
      <div class="panel-item" style="top:300px"><div class="icon-ring" role="img" aria-label="First aid kit icon"><i style="border-radius:6px;height:26px;background:#e8414c"></i></div><p>Mandatory sanitation in all places - use of disinfection available on a large scale.</p></div>
      <div class="panel-item" style="top:375px"><div class="icon-ring"><svg width="34" height="34" viewBox="0 0 34 34" aria-hidden="true"><circle cx="17" cy="17" r="14" fill="#fde3d6" stroke="#e8414c" stroke-width="4"/><path d="M7 27L27 7" stroke="#e8414c" stroke-width="4"/></svg></div><p>Ability to track and trace infected patients and contacts on a live basis and across the country and ability to react quickly to any unusual trends or outbreaks.</p></div>
    </div>

    <div class="abs blob-bl"></div>
    <div class="abs base-line"></div>
  </div>
</section>

<section class="sheet sheet--back">
  <div class="page">
    <div class="abs header">PHASED COVID-19 LOCKDOWN EXIT<br>STRATEGY PLAN</div>

    <div class="art" style="left:55px;top:82px;width:64px;height:64px;background:var(--peach-light)" role="img" aria-label="Cloud icon"></div>
    <div class="abs stage-tag" style="left:150px;top:85px">STAGE 1:</div>
    <p class="abs lead" style="left:155px;top:128px;width:380px">To enter this stage, additional to the general requirements, the Effective Reproduction Number (Rt) must be less than 1 and the death rate at less than 3%.</p>
    <div class="abs seq-head" style="left:64px;top:177px">The economy and social activities can resume in this sequence:</div>
    <ol class="seq" style="left:64px;top:205px;width:215px">
      <li style="height:30px"><em>01</em>Elderly (60+ years old) and vulnerable individuals should continue to self-isolate.</li>
      <li style="height:28px"><em>02</em>No more than 5 people maximum gathering at a time in public areas and at work.</li>
      <li style="height:48px"><em>03</em>Work from home should continue whenever and as much as possible. Social distancing should continue to be re-enforced in public areas, at work and in all areas reopened.</li>
      <li style="height:38px"><em>04</em>Non-essential travel should be minimized between cities and regions (and within cities and regions where covid-19 infections are still a risk)</li>
      <li><em>05</em>Large businesses (300 people and more, manufacturing, services, etc.) can reopen progressively. Common areas should remain closed (cafeteria, restaurant, gym, meeting rooms of no more than 5 people).</li>
    </ol>
    <ol class="seq" style="left:300px;top:205px;width:240px">
      <li style="height:30px"><em>06</em>Small businesses (300 people and less) can reopen as well with the same conditions as large businesses.</li>
      <li style="height:48px"><em>07</em>Commercial shops can reopen. Shops should control the flow of people in their facilities not to exceed 30% at a time of standard capacity. Shops should provide disinfectant and temperature control at entry.</li>
      <li style="height:66px"><em>08</em>Pharmacies will continue to be open. However, they must make available disinfectant for use by clients and will continue to comply with social distancing. Pharmacies should limit the number of client/patient in their stores not to exceed 30% of the standard capacity.</li>
      <li><em>10</em>Transportation (buses, taxis, airlines) will resume progressively. No air travels permitted in and out of Covid-19 known hotspots, locally or internationally. Entry to country should be limited and strictly controlled.</li>
    </ol>

    <svg class="abs" style="left:55px;top:428px" width="62" height="62" viewBox="0 0 62 62" aria-hidden="true">
      <circle cx="31" cy="31" r="29" fill="#f04157"/>
      <path d="M31 31V2A29 29 0 0 1 60 31z" fill="#fbd9a6"/>
      <path d="M31 31H60A29 29 0 0 1 31 60z" fill="#f9a03f"/>
    </svg>
    <div class="abs stage-tag" style="left:135px;top:438px;width:128px">STAGE 2</div>
    <div class="stage-col" style="left:58px;top:496px;width:225px">
      <p class="lead">To enter stage 2 of the Covid-19 Exit Strategy, compliance to the general requirements is compulsory, additional to a successful Stage 1 outcome. The Effective Reproduction Number (Rt) for Stage 2 must be less than 0.5 and the death rate stabilized at less than 2%.</p>
      <div class="seq-head">The economy and social activities can resume in this sequence:</div>
      <ol class="seq">
        <li><em>01</em>Elderly (60+ years old) and vulnerable individuals should continue to self-isolate as much as possible.</li>
        <li><em>02</em>No more than 10 people maximum gathering at a time in public areas and at work.</li>
        <li><em>03</em>Work from home should if possible or for jobs that do not have to be necessarily in an office setup.</li>
        <li><em>04</em>Social distancing can be relaxed. However people should continue to wear masks and use disinfectants.</li>
        <li><em>05</em>Travel can resume between cities and regions. The same containment restrictions should apply to any existing hotspot.</li>
        <li><em>06</em>Elective surgeries can resume in hospitals and clinics that are equipped to comply with all general requirements.</li>
      </ol>
    </div>

    <div class="abs divider"></div>

    <div class="abs" style="left:300px;top:428px;width:80px;height:52px;border-radius:10px;background:linear-gradient(90deg,#4ab0e6,#2f86d1)" role="img" aria-label="World map with a highlighted hotspot"></div>
    <div class="abs stage-tag" style="left:395px;top:438px;width:128px">STAGE 3</div>
    <div class="stage-col" style="left:307px;top:492px;width:232px">
      <p class="lead">To enter stage 3 of the Covid-19 Exit Strategy, compliance to the general requirements is compulsory, additional to a successful Stage 2 outcome. The Effective Reproduction Number (Rt) for Stage 3 must be less than 0.3 and the death rate stabilized at less than 1%.</p>
      <div class="seq-head">The economy and social activities can resume in this sequence:</div>
      <ol class="seq">
        <li><em>01</em>Elderly (60+ years old) and vulnerable individuals may resume all previously exercised activities without restrictions.</li>
        <li><em>02</em>Restrictions as to the number of people gathering together can be lifted. Social distancing can be relaxed. However, wear of masks may continue.</li>
        <li><em>03</em>Travel can resume between cities and regions and out of country travel. The same containment restrictions as Stage 1 and 2 would continue to apply to any existing hotspot.</li>
        <li><em>04</em>All hospital and clinic surgeries can resume in hospitals in compliance with standard hospital and health care procedures.</li>
        <li><em>05</em>Large businesses (300 people and more, manufacturing, services, etc.) will resume normal business practices. Wear of masks is recommended but not mandatory.</li>
      </ol>
    </div>

    <div class="abs blob-br"></div>
    <div class="abs base-line"></div>
  </div>
</section>

</body>
</html>
```